Talent Harbor Posts - Built for the Industry, by the Industry.

Looking for an email marketing Infographic I can send out via email to target Recruitment Firms letting them know we are launched! As of January 7th VORANTE is no longer allowing Recruitment Firms to post on their site unless you pay thousands of dollars a month. We are launching a site just for Recruiters to showcase their jobs. I have attached the almost completed website and a mocked up version of a simple infographic but we are looking for a WOW design that can get emailed out to 1000's of Recruitment Firms and they will just have to click the image to be taken to our site. I have added the colors and raleway - medium is the font on our site. Blue RGB: 8/113/182 Navy RGB: 27/32/48

Recruitment Firms Across Canada and the USA

• WOW Factor, use of our Brand and Colours - raleway - medium is the font on our site. Blue RGB: 8/113/182 Navy RGB: 27/32/48. Our Logo and I have also attached our Landing Page ... down below.
• You can use "It's Time for Something New" or I'd be open to other ideas and taglines ... I'd like to see No Sponsored Jobs / No Pay-Per-Click / Flat Rates Only ...
• Our tagline is also - Built for the Industry, by the Industry"

```html
<!DOCTYPE html>
<html lang="en">
<head>
<meta charset="utf-8">
<title>Talent Harbor Posts – It's Time for Something New</title>
<link rel="stylesheet" href="https://fonts.googleapis.com/css2?family=Jost:wght@400;500&family=Montserrat:wght@400;500;600&family=Josefin+Sans:wght@400;600&display=swap">
<style>
  :root {
    --paper: #ffffff;
    --ink-grey: #6b6b6b;
    --rule-grey: #8a8486;
    --night: #23232a;
    --footer: #363440;
    --ribbon-ink: #34343f;
    --yellow: #fecb2f;
    --yellow-fold: #8f6f04;
    --green: #50dc00;
    --green-fold: #3a9e02;
    --sky: #6ac2fb;
    --white: #ffffff;
    --soft-white: #e4e4e8;
    --social-bg: #f6f6f6;
    --social-1: #4f72b8;
    --social-2: #6fc7ef;
    --social-3: #1b77b7;
  }
  * { box-sizing: border-box; margin: 0; padding: 0; }
  html, body { width: 804px; height: 1200px; overflow: hidden; background: var(--paper); }
  .canvas { position: relative; width: 804px; height: 1200px; background: var(--paper); font-family: "Montserrat", sans-serif; }

  .top-tagline {
    position: absolute; left: 150px; top: 80px; width: 498px;
    text-align: center; font-size: 19px; letter-spacing: 1.4px; color: var(--ink-grey);
    font-weight: 500; padding-bottom: 10px; border-bottom: 2px solid var(--rule-grey);
  }

  .hero { position: absolute; left: 0; top: 163px; width: 804px; height: 642px; overflow: hidden; }
  .hero-backdrop {
    position: absolute; inset: 0;
    background: linear-gradient(180deg, #2f333d 0%, #3b3f48 25%, #34363f 55%, #25252c 80%, var(--night) 100%);
  }
  .hero-kicker {
    position: absolute; top: 18px; left: 0; width: 804px; text-align: center;
    font-family: "Jost", sans-serif; font-size: 29px; line-height: 40px; color: var(--soft-white); letter-spacing: 0.5px;
    white-space: nowrap;
  }
  .hero-kicker::before, .hero-kicker::after {
    content: ""; position: absolute; top: 20px; width: 138px; height: 2px; background: var(--white);
  }
  .hero-kicker::before { left: 142px; }
  .hero-kicker::after { left: 520px; }
  .hero-title {
    position: absolute; top: 44px; left: 0; width: 804px; text-align: center;
    font-family: "Jost", sans-serif; font-weight: 500; font-size: 60px; line-height: 72px; color: var(--white); letter-spacing: 0.3px;
    white-space: nowrap;
  }
  .ribbons { position: absolute; left: 0; top: 0; }
  .ribbon-label { font-family: "Josefin Sans", sans-serif; font-size: 29px; fill: var(--ribbon-ink); letter-spacing: 0.6px; }

  .cta {
    position: absolute; left: 200px; top: 541px; width: 398px; height: 48px;
    border: 2px solid var(--white); border-radius: 24px;
    display: flex; align-items: center; justify-content: center;
    color: var(--white); font-size: 19px; font-weight: 500; text-decoration: none; letter-spacing: 0.3px;
    white-space: nowrap;
  }

  .footer { position: absolute; left: 0; top: 805px; width: 804px; height: 240px; background: var(--footer); color: var(--white); }
  .brand { position: absolute; left: 222px; top: 36px; width: 353px; height: 90px; border-bottom: 2px solid var(--white); }
  .brand-mark { position: absolute; left: 6px; top: 10px; width: 62px; height: 62px; border-radius: 50%; background: var(--white); }
  .brand-name {
    position: absolute; left: 84px; top: 4px; width: 262px;
    font-size: 24px; line-height: 27px; font-weight: 500; letter-spacing: 0.5px; color: var(--white);
  }
  .brand-name span { display: block; white-space: nowrap; }
  .brand-line { position: absolute; left: 84px; top: 70px; font-size: 8px; line-height: 10px; font-weight: 600; letter-spacing: 0.3px; white-space: nowrap; }
  .contact { position: absolute; left: 0; width: 804px; text-align: center; font-size: 15px; white-space: nowrap; }
  .contact strong { font-weight: 500; }
  .contact-main { top: 156px; }
  .contact-address { top: 191px; }
  .divider { margin: 0 12px; }

  .social { position: absolute; left: 298px; top: 1088px; width: 198px; height: 64px; background: var(--social-bg); }
  .social-dot { position: absolute; top: 8px; width: 48px; height: 48px; border-radius: 50%; }
  .social-dot.one { left: 18px; background: var(--social-1); }
  .social-dot.two { left: 76px; background: var(--social-2); }
  .social-dot.three { left: 134px; background: var(--social-3); }
</style>
</head>
<body>
<main class="canvas">
  <p class="top-tagline">BUILT FOR THE INDUSTRY, BY THE INDUSTRY</p>

  <section class="hero">
    <div class="hero-backdrop" role="img" aria-label="Night skyline of a city with lit towers"></div>
    <p class="hero-kicker">ITS TIME FOR</p>
    <h1 class="hero-title">SOMETHING NEW</h1>

    <svg class="ribbons" width="804" height="642" viewBox="0 163 804 642">
      <polygon points="100,362 475,383 475,461 118,461" fill="var(--yellow)"/>
      <polygon points="118,461 700,466 362,486" fill="var(--yellow-fold)"/>
      <polygon points="362,486 700,466 685,565 362,562" fill="var(--green)"/>
      <polygon points="115,568 362,562 685,565 425,592" fill="var(--green-fold)"/>
      <polygon points="115,568 425,592 425,668 152,668" fill="var(--sky)"/>
      <text class="ribbon-label" x="132" y="422">NO SPONSORED JOB</text>
      <text class="ribbon-label" x="383" y="527">NO PAY PER CLICK</text>
      <text class="ribbon-label" x="148" y="636">FLAT RATES ONLY</text>
    </svg>

    <a class="cta" href="#">CLICK HERE TO KNOW MORE</a>
  </section>

  <footer class="footer">
    <div class="brand">
      <span class="brand-mark"></span>
      <p class="brand-name"><span>TALENT HARBOR</span><span>POSTS</span></p>
      <span class="brand-line">BUILT FOR THE INDUSTRY, BY THE INDUSTRY</span>
    </div>
    <p class="contact contact-main"><strong>Phone:</strong> 555 .0142.7788<span class="divider">|</span><strong>Email:</strong> hello@talentharborposts.com</p>
    <p class="contact contact-address">Havenkade 42, 1000 AB Lindeport, The Netherlands</p>
  </footer>

  <nav class="social" aria-label="Social links">
    <span class="social-dot one"></span>
    <span class="social-dot two"></span>
    <span class="social-dot three"></span>
  </nav>
</main>
</body>
</html>
```